Brindle Works - Fast, Efficient and Gas Mainteance for Domestic, Commercial and Industrial clients

We are in the process of purchasing a new business and would like to get a new logo and business card.
Business is a gas maintenance business that also does new gas installations.
Has been established since 1988.
Services include:
Install all types of gas appliances & equipment inc. hot water units
Maintain / repair / replace all types of gas appliances & equipment

Target Market(s)

Domestic, Commercial and Industrial clients

Industry/Entity Type

Business

Contact Information for Business Card

admin@brindleworks-example.com.au
07 5981 4726
Brindle Works PTY LTD

Logo Text

Gas Fitting & Plumbing Maintenance Specialists

Font styles to use
Sans Serif

Requirements
Must have
• Logo
• Business name, contact number, email address, web address
• Domestic | Commercial | Industrial Est Since 1988
Nice to have
• Possibly a black card with a flame logo to one side
Should not have
• Spelling errors

```html
<!DOCTYPE html>
<html lang="en">
<head>
<meta charset="utf-8">
<title>Brindle Works – Business Card</title>
<link href="https://fonts.googleapis.com/css2?family=Montserrat:wght@400;500&display=swap" rel="stylesheet">
<style>
  :root {
    --backdrop: #e9e4dc;
    --card: #050404;
    --gold: #e9b446;
    --flame: #f08a1c;
    --ember: #a8320a;
    --glow: #ffb347;
  }
  * { margin: 0; padding: 0; box-sizing: border-box; }
  html, body {
    width: 1200px; height: 569px; overflow: hidden;
    background: var(--backdrop);
  }
  .canvas { position: relative; width: 1200px; height: 569px; }

  .card {
    position: absolute; top: 166px;
    width: 402px; height: 237px;
    background: var(--card);
    border-radius: 9px;
    overflow: hidden;
    box-shadow: 0 4px 10px rgba(0,0,0,0.35);
    font-family: "Montserrat", sans-serif;
  }
  .card--front { left: 175px; }
  .card--back  { left: 624px; }

  .flames {
    position: absolute; left: 0; right: 0; bottom: 0; height: 150px;
    background:
      radial-gradient(ellipse 30% 70% at 85% 100%, var(--glow) 0%, var(--flame) 30%, rgba(168,50,10,0.5) 60%, transparent 80%),
      radial-gradient(ellipse 40% 45% at 20% 100%, var(--flame) 0%, var(--ember) 45%, transparent 80%),
      linear-gradient(to bottom, transparent 0%, rgba(120,30,5,0.35) 60%, rgba(220,90,20,0.7) 100%);
  }

  .brand {
    position: absolute; left: 25px; top: 36px;
    display: flex; align-items: center; gap: 10px;
  }
  .brand__dot {
    width: 22px; height: 22px; border-radius: 50%;
    background: var(--flame);
  }
  .brand__name {
    color: var(--flame);
    font-size: 21px; font-weight: 500;
    letter-spacing: 1px; text-transform: uppercase;
    line-height: 1;
  }

  .list {
    position: absolute; list-style: none;
    color: var(--gold);
    font-size: 8.5px; font-weight: 400;
    font-variant: small-caps; letter-spacing: 0.8px;
  }
  .list li { position: relative; padding-left: 7px; }
  .list li::before {
    content: ""; position: absolute; left: 0; top: 50%;
    width: 2.5px; height: 2.5px; margin-top: -1px;
    border-radius: 50%; background: var(--gold);
  }
  .list--sectors { left: 67px; top: 100px; line-height: 10.6px; }

  .brand-mark {
    position: absolute; left: 24px; top: 38px;
    width: 22px; height: 22px; border-radius: 50%;
    background: var(--flame);
  }
  .list--contact { left: 70px; top: 33px; font-size: 9.5px; line-height: 14.5px; }
</style>
</head>
<body>
<main class="canvas">
  <section class="card card--front">
    <div class="flames" role="img" aria-label="Photograph of orange flames and embers rising along the bottom of the card"></div>
    <div class="brand">
      <span class="brand__dot"></span>
      <span class="brand__name">Brindle Works</span>
    </div>
    <ul class="list list--sectors">
      <li>Domestic</li>
      <li>Commercial</li>
      <li>Industrial Est Since 1988</li>
    </ul>
  </section>

  <section class="card card--back">
    <div class="flames" role="img" aria-label="Photograph of orange flames and embers rising along the bottom of the card"></div>
    <span class="brand-mark"></span>
    <ul class="list list--contact">
      <li>admin@brindleworks-example.com.au</li>
      <li>07 5981 4726</li>
      <li>Brindle Works PTY LTD</li>
    </ul>
  </section>
</main>
</body>
</html>
```